Sponsors Ad for the KTWLA 75th Anniversary Gala

This ad is to congratulate the awardees and the KTWLA for its 75th anniversary. Brightmoor is a sponsor and we get a full screen ad as part of our sponsorship. I have attached the spec sheet for the full screen ad, a PDF of the gala website with the people being honored and the information of that they are celebrating the 75th anniversary, I also attached my logo. My website is www.brightmoorqa.example if you want to get any information from that. See sample ads of others from past years uploaded.

Target Market(s)

Attendees at the Gala (attorneys will be attending)

Industry/Entity Type

legal

Requirements
Must have
• Congratulations to the award recipients and the KTWLA for 75th Anniv.
Nice to have
• Reference to the high standard and quality of the work done by Brightmoor but subtle as this is not the primary purpose.
Should not have
• dates and times

```html
<!DOCTYPE html>
<html lang="en">
<head>
<meta charset="utf-8">
<title>KTWLA 75th Anniversary Gala – Brightmoor Sponsor Ad</title>
<link rel="stylesheet" href="https://fonts.googleapis.com/css2?family=Poppins:wght@500;600;700;800&display=swap">
<style>
  :root {
    --gold: #c08f33;
    --navy: #132c55;
    --navy-deep: #0f2243;
    --ink: #111111;
    --paper: #ffffff;
  }
  * { margin: 0; padding: 0; box-sizing: border-box; }
  html, body { width: 1089px; height: 1200px; overflow: hidden; background: var(--gold); }
  body { font-family: "Poppins", sans-serif; position: relative; }

  .ad-panel {
    position: absolute; left: 116px; top: 113px;
    width: 856px; height: 973px;
    background: var(--paper); overflow: hidden;
  }
  .panel-art { position: absolute; inset: 0; width: 856px; height: 973px; }

  .copy { position: absolute; left: 46px; white-space: nowrap; }

  .org-title {
    top: 40px; color: var(--gold);
    font-weight: 600; font-size: 62px; line-height: 61px; letter-spacing: -0.5px;
  }
  .gala-title {
    top: 160px; color: var(--navy);
    font-weight: 800; font-size: 63px; line-height: 62px; letter-spacing: -0.5px;
  }
  .tagline {
    top: 348px; color: var(--ink);
    font-weight: 600; font-size: 23.5px; line-height: 25px;
  }
  .rule { position: absolute; left: 46px; width: 400px; height: 1px; background: var(--gold); }
  .rule--top { top: 434px; }
  .rule--bottom { top: 564px; }

  .congrats-label {
    top: 439px; color: var(--gold);
    font-weight: 700; font-size: 26.5px; line-height: 30px;
  }
  .congrats-text {
    top: 468px; color: var(--ink);
    font-weight: 600; font-size: 23.5px; line-height: 27px;
  }
  .performance-label {
    top: 599px; color: var(--navy);
    font-weight: 600; font-size: 30px; line-height: 36px;
  }
  .awards-title {
    top: 632px; color: var(--gold);
    font-weight: 800; font-size: 47.5px; line-height: 49px;
  }

  .sponsor { top: 808px; display: flex; align-items: center; gap: 14px; }
  .sponsor-mark { width: 44px; height: 44px; background: var(--navy); }
  .sponsor-name {
    color: var(--navy); font-weight: 600; font-size: 40px; line-height: 44px; letter-spacing: 1px;
  }
  .sponsor-url {
    top: 905px; color: var(--navy);
    font-weight: 600; font-size: 19px; line-height: 24px; letter-spacing: 0.3px;
  }
</style>
</head>
<body>
  <main class="ad-panel">
    <svg class="panel-art" viewBox="0 0 856 973">
      <defs>
        <linearGradient id="photoTone" x1="0" y1="0" x2="1" y2="1">
          <stop offset="0" stop-color="#0f2243"/>
          <stop offset="0.55" stop-color="#17305b"/>
          <stop offset="1" stop-color="#0f2243"/>
        </linearGradient>
      </defs>
      <polygon points="510,642 445,973 423,973" fill="var(--gold)"/>
      <polygon role="img" aria-label="Navy-toned photo of two attorneys reviewing documents together"
               points="639,0 856,0 856,973 445,973" fill="url(#photoTone)"/>
    </svg>

    <h1 class="copy org-title">THE KTWLA<br>FOUNDATION</h1>
    <h2 class="copy gala-title">75TH<br>ANNIVERSARY<br>GALA</h2>
    <p class="copy tagline">Honoring Extraordinary<br>Leadership and Lasting Impact</p>

    <div class="rule rule--top"></div>
    <h3 class="copy congrats-label">CONGRATULATIONS</h3>
    <p class="copy congrats-text">To The KTWLA And This Year's<br>Honorees On Seventy-Five Years<br>Of Service And Justice.</p>
    <div class="rule rule--bottom"></div>

    <p class="copy performance-label">SPECIAL PERFORMANCE BY</p>
    <p class="copy awards-title">CHAMPION OF<br>JUSTICE AWARDS</p>

    <div class="copy sponsor">
      <span class="sponsor-mark"></span>
      <span class="sponsor-name">BRIGHTMOOR</span>
    </div>
    <p class="copy sponsor-url">WWW.BRIGHTMOORQA.EXAMPLE</p>
  </main>
</body>
</html>
```